a Label for a candle jar and its gift box

I would like a label that is modern minimalist for candles jars. These jars are colored as white, amber and black. I am thinking maybe foiling gold/silver background with logo only and maybe company name in different color that suits the foiling background color/s. I would like a high quality luxurious design that shows the preciousness of this candle. I am open to any ideas you might have for the design but so far I have used a logo only on the jar which I really like BUT I still feel that it is not enough branding for people when you only show them the logo so I am considering adding the business name. Again, I am open to both ideas (with logo only or logo with business name (Silken Meadow).

IMPORTANT: YOU MAY IGNORE MY DESIGN COMPLETELY AND DO YOUR OWN ONE AS LONG AS YOU KERP THE LOGO DESIGN. YOU MAY ALSO ADJUST THE LOGO A BIT TO SUIT YOUR DESIGN. - sorry im using capital letters to show importance but im not yelling :)

UPDATE: To clarify, I have uploaded a video called Corvel in the box to show what the current product look like. It is a corvel jar with a logo only and the jar box has a window that shows the jar with the logo on it and the back of that jar box has a bigger version of the label that has more details (i.e. Fragrance name and website link). So to make it clear, I would like to have two versions of the lables: 1. on the jar with minimal info (logo only or logo with the business name) 2. Bigger version of the label with more info to put on the back of the jar box - as described above. The dimensions of the jars are as per this link https://www.lunaxo-example.com.au/corvel-medium-base-and-flat-lid-amber-packed-with-lid-on/ The dimensions of the jar box as per this link https://www.lunaxo-example.com.au/corvel-medium-flat-lid-candle-box-with-window-beige/ Looking forward to some artistic productions :)

Update #2: Tues 25 Dec 18 1. I have uploaded the photo which has the logo with the name 'Silken Meadow' below it just for a reference. However, I would like the designer to modify the current font and NOT to use it as the word 'of in the phrase 'Silken Meadow' does not come out clear enough after printing. 2. I would like the designer NOT to create a design that will require a clear sticker/label for printing. 3. I have attached the photos of my current designs on the jars or the jar box just as a reference but please do NOT just use the same fonts and only change background. I am hoping to see something different and more professional than my own design :) Thank you very much!

Font styles to use
Decorative
Script

Requirements
Must have
• I would like them to fit on the three colors of the jars below - white, amber and black. Below is a link to how the jar looks like https://www.lunaxo-example.com.au/candle-making-supplies/candle-jars/corvel-candle-jars/?glassware_colour=415,443,417&glassware_size=268
Nice to have
• I would like to have a modern design which is suitable for both feminine and musculine.
Should not have
• shouldnt have so much writing on it!

```html
<!DOCTYPE html>
<html lang="en">
<head>
<meta charset="utf-8">
<title>Silken Meadow – Velvet Peony Candle Labels</title>
<link rel="stylesheet" href="https://fonts.googleapis.com/css2?family=Oswald:wght@400&family=Raleway:wght@200&display=swap">
<style>
  :root {
    --canvas-bg: #ffffff;
    --box-black: #1b1b1b;
    --brown: #5a1f08;
    --brown-text: #6b2a0a;
    --gold-light: #e8e86a;
    --gold-mid: #c9c24a;
    --gold-dark: #857024;
    --site-grey: #9a9a9a;
  }
  html, body {
    margin: 0;
    padding: 0;
    overflow: hidden;
    background: var(--canvas-bg);
  }
  .canvas {
    width: 1200px;
    height: 1000px;
    position: relative;
    overflow: hidden;
    background: var(--canvas-bg);
  }
  .canvas svg {
    display: block;
  }
  .label-name {
    font-family: "Oswald", sans-serif;
    font-weight: 400;
    fill: var(--brown-text);
    letter-spacing: 3px;
  }
  .label-fragrance {
    font-family: "Oswald", sans-serif;
    font-weight: 400;
    fill: var(--brown-text);
  }
  .box-website {
    font-family: "Raleway", sans-serif;
    font-weight: 200;
    fill: var(--site-grey);
    letter-spacing: 1px;
  }
</style>
</head>
<body>
<main class="canvas">
  <svg width="1200" height="1000" viewBox="0 0 1200 1000" xmlns="http://www.w3.org/2000/svg">
    <defs>
      <linearGradient id="gold-face" x1="0" y1="0" x2="1" y2="0">
        <stop offset="0" style="stop-color: var(--gold-dark)"/>
        <stop offset="0.3" style="stop-color: var(--gold-mid)"/>
        <stop offset="0.5" style="stop-color: var(--gold-light)"/>
        <stop offset="0.75" style="stop-color: var(--gold-mid)"/>
        <stop offset="1" style="stop-color: var(--gold-dark)"/>
      </linearGradient>
      <linearGradient id="gold-rim" x1="0" y1="0" x2="1" y2="1">
        <stop offset="0" style="stop-color: var(--gold-dark)"/>
        <stop offset="0.45" style="stop-color: var(--gold-light)"/>
        <stop offset="1" style="stop-color: var(--gold-dark)"/>
      </linearGradient>

      <g id="round-label" class="round-label">
        <circle class="label-rim" r="213" fill="url(#gold-rim)"/>
        <circle class="label-brown-ring" r="197" fill="var(--brown)"/>
        <circle class="label-inner-line" r="190" fill="#f3efc8"/>
        <circle class="label-face" r="188" fill="url(#gold-face)"/>
        <text class="label-name" x="0" y="-30" font-size="30" text-anchor="middle">SILKEN MEADOW</text>
        <line class="label-rule" x1="-122" y1="63" x2="123" y2="63" stroke="var(--brown)" stroke-width="1.6"/>
        <text class="label-fragrance" x="0" y="114" font-size="46" text-anchor="middle" textLength="200" lengthAdjust="spacingAndGlyphs">VELVET PEONY</text>
        <line class="label-rule" x1="-101" y1="126" x2="102" y2="126" stroke="var(--brown)" stroke-width="1.6"/>
      </g>
    </defs>

    <!-- Jar-box back label, large -->
    <use href="#round-label" class="label-large" transform="translate(273 497)"/>

    <!-- Gift box back panel -->
    <g class="gift-box-panel">
      <rect x="536" y="337" width="330" height="375" fill="var(--box-black)"/>
      <use href="#round-label" transform="translate(701 524) scale(0.634)"/>
      <text class="box-website" x="701" y="696" font-size="12" text-anchor="middle">www.silkenmeadow.com.au</text>
    </g>

    <!-- Jar front label, small -->
    <use href="#round-label" class="label-small" transform="translate(1020 557) scale(0.376)"/>
  </svg>
</main>
</body>
</html>
```